Product labels for new supplements business targeting high performing creative people

I need a label design for different supplements like Whey, BCAA, Melatonin etc. that I could customize for each use case separately.

The brand is called lanternfolk.life, and it would be the first design of the labels. We haven't sold any products yet, but the target audience is people with growth mindset, people who want to be as efficient as possible and are constantly looking to improve their lifestyle. As part of that, they are also working out, but don't know much about supplements yet. Mostly people between 20-34.

I don't have a too specific idea of the expected design, though it should be light, warm, smart and minimalist, maybe have some patterns. It should looks smart and clean (and expensive). Orange and golden might be the additional colors for white. I have attached the templates of some products that I plan to sell and also the logo of the brand.

Here's what I have used for inspiration:
Brands that I like and are somewhat similar in concept: https://www.vimqera.com/ (!!specially the way they
bring "how the product helps them" in focus, not "what the product is" & https://www.pobri.care/ &
https://www.selvoda.com/sport/ & https://en.kambelo.fr/ &
https://gridmarket.com/profiles/corawellhaldesign/designs/417586

Here's how different products look like: https://prodaxel.com/catalog

Target Market(s)

target audience is people with growth mindset, people who want to be as efficient as possible and are constantly looking to improve their lifestyle. As part of that, they are also working out, but don't know much about supplements yet. Mostly people between 20-34.

Industry/Entity Type

Supplements

Font styles to use
Sans Serif

Colors
FFC000
F8CF3A
FAE287
FDF2CF
FEFAEE
F0912C
F2A743
F7CA91
FBE8D2
FDF5EE
EE7325
F08F49
F5BC92
FAE3D3
FDF4ED

Requirements
Must have
• Clean, smart and minimalist design that can be applied for different products in different sizes, like Whey protein, BCAA, vitamins etc. available here: https://prodaxel.com/catalog
Nice to have
• Patterns, expensive look
Should not have
• Doodles, too many colors

```html
<!DOCTYPE html>
<html lang="en">
<head>
<meta charset="utf-8">
<title>lanternfolk.life supplement labels</title>
<link rel="stylesheet" href="https://fonts.googleapis.com/css2?family=Questrial&family=Quicksand:wght@400;500;600&family=Arimo:wght@400;700&family=Archivo+Black&display=swap">
<style>
  :root {
    --backdrop: #FCE98E;
    --paper: #FFFFFF;
    --ink: #2B2B2B;
    --ink-soft: #555555;
    --gold: #F8C23A;
    --gold-deep: #F2B01E;
    --gold-pale: #FDEBB2;
    --gold-mist: #FEF5D8;
    --brand-dot: #EE7325;
  }
  * { box-sizing: border-box; margin: 0; padding: 0; }
  html, body { width: 1200px; height: 1151px; overflow: hidden; }
  body {
    background: var(--backdrop);
    position: relative;
    font-family: "Quicksand", sans-serif;
    color: var(--ink);
  }

  .panel {
    position: absolute;
    background: var(--paper);
    overflow: hidden;
  }
  .panel--front, .panel--back { top: 40px; width: 340px; height: 440px; }
  .panel--bcaa { left: 45px; }
  .panel--protein { left: 430px; }
  .panel--back { left: 815px; }

  .wave-band {
    position: absolute; left: 0; right: 0; bottom: 0; height: 40px;
    background: linear-gradient(180deg, var(--gold-mist), var(--gold-pale));
  }
  .ring {
    position: absolute; border-radius: 50%;
    background: radial-gradient(circle at 40% 40%, var(--gold-mist), var(--gold-pale));
  }

  .brand {
    position: absolute; display: flex; align-items: center; gap: 7px;
    font-family: "Quicksand", sans-serif; font-weight: 600; color: var(--ink);
    white-space: nowrap;
  }
  .brand__dot { border-radius: 50%; background: var(--brand-dot); }

  .product-title {
    position: absolute; font-family: "Questrial", sans-serif;
    font-weight: 400; line-height: 1; letter-spacing: 1px; color: var(--ink);
    white-space: nowrap;
  }
  .product-title .accent { color: var(--gold); }
  .product-flavour {
    position: absolute; font-family: "Questrial", sans-serif;
    color: var(--ink-soft); letter-spacing: 1px; line-height: 1; white-space: nowrap;
  }
  .benefit { position: absolute; font-weight: 500; line-height: 1.4; color: var(--ink); }
  .category { position: absolute; font-weight: 600; letter-spacing: 0.5px; color: var(--ink); white-space: nowrap; }
  .net-weight { position: absolute; color: var(--ink-soft); white-space: nowrap; }

  /* front panels */
  .panel--front .brand { left: 32px; top: 44px; font-size: 21px; }
  .panel--front .brand__dot { width: 12px; height: 12px; }
  .panel--front .benefit { left: 32px; width: 285px; font-size: 14px; }
  .panel--front .category { left: 32px; top: 342px; font-size: 14px; }
  .panel--front .net-weight { left: 32px; top: 368px; font-size: 13px; }

  /* back text */
  .usage { position: absolute; }
  .usage__heading { font-weight: 600; color: var(--gold-deep); letter-spacing: 0.5px; }
  .usage__text { color: var(--ink); line-height: 1.4; }
  .usage__warning { text-transform: uppercase; line-height: 1.35; }
  .usage__note { line-height: 1.35; }

  .panel--back .usage { left: 30px; top: 100px; width: 290px; }
  .panel--back .usage__heading { font-size: 12.5px; margin-bottom: 1px; }
  .panel--back .usage__text { font-size: 11.5px; margin-bottom: 12px; }
  .panel--back .usage__warning { font-size: 10px; margin-bottom: 10px; }
  .panel--back .usage__note { font-size: 10px; }

  /* full wrap */
  .panel--wrap { left: 50px; top: 560px; width: 1100px; height: 430px; }
  .panel--wrap .wave-band { height: 30px; }
  .wrap-col { position: absolute; top: 0; bottom: 30px; }
  .wrap-col--usage { left: 0; width: 360px; }
  .wrap-col--front { left: 370px; width: 360px; }
  .wrap-col--facts { left: 740px; width: 360px; }

  .wrap-col--usage .usage { left: 26px; top: 100px; width: 300px; }
  .wrap-col--usage .usage__heading { font-size: 12px; margin-bottom: 1px; }
  .wrap-col--usage .usage__text { font-size: 12px; margin-bottom: 22px; line-height: 1.35; }
  .wrap-col--usage .usage__warning { font-size: 10px; margin-bottom: 12px; }
  .wrap-col--usage .usage__note { font-size: 10px; }

  .wrap-col--front .brand { left: 32px; top: 30px; font-size: 19px; }
  .wrap-col--front .brand__dot { width: 11px; height: 11px; }
  .wrap-col--front .benefit { left: 32px; top: 262px; width: 290px; font-size: 12px; font-weight: 500; }
  .wrap-col--front .category { left: 32px; top: 346px; font-size: 12.5px; font-weight: 500; }
  .wrap-col--front .net-weight { left: 32px; top: 368px; font-size: 12px; }

  .facts {
    position: absolute; left: 22px; top: 36px; width: 322px;
    border: 2px solid #000; padding: 4px 5px 6px;
    font-family: "Arimo", sans-serif; color: #000;
  }
  .facts__title { font-family: "Archivo Black", sans-serif; font-size: 26px; line-height: 1.05; white-space: nowrap; }
  .facts__serving { font-size: 11.5px; line-height: 1.2; padding: 3px 0 2px; border-bottom: 8px solid #000; }
  .facts__row { display: flex; font-size: 11.5px; padding: 2px 0; border-bottom: 1px solid #000; }
  .facts__row--head { font-weight: 700; font-size: 11px; line-height: 1.05; border-bottom: 4px solid #000; text-align: right; }
  .facts__row--last { border-bottom: 4px solid #000; }
  .facts__name { flex: 1; }
  .facts__amount { width: 80px; text-align: right; }
  .facts__dv { width: 50px; text-align: right; }
  .facts__footnote { font-size: 11.5px; padding-top: 4px; }
  .ingredients { position: absolute; left: 26px; top: 232px; width: 310px; font-family: "Arimo", sans-serif; font-size: 11.5px; line-height: 1.2; color: #000; }
  .maker { position: absolute; left: 26px; top: 338px; font-family: "Arimo", sans-serif; font-weight: 700; font-size: 9.5px; line-height: 1.3; color: #111; }
</style>
</head>
<body>

<section class="panel panel--front panel--bcaa">
  <div class="brand"><span class="brand__dot"></span>lanternfolk.life</div>
  <h1 class="product-title" style="left:30px;top:118px;font-size:46px;">BCAA <span class="accent">2:1:1</span></h1>
  <p class="product-flavour" style="left:32px;top:172px;font-size:22px;">WILD BERRY</p>
  <div class="ring" role="img" aria-label="Soft golden line-pattern disc" style="left:32px;top:224px;width:38px;height:38px;"></div>
  <p class="benefit" style="top:278px;">Essential branched chain aminoacids BCAA increases muscles growth, reduce fatigue*</p>
  <p class="category">DIETARY SUPPLEMENT</p>
  <p class="net-weight">Net Wt. 300 g (10.58oz)</p>
  <div class="wave-band" role="img" aria-label="Golden wavy-line pattern band"></div>
</section>

<section class="panel panel--front panel--protein">
  <div class="brand"><span class="brand__dot"></span>lanternfolk.life</div>
  <h1 class="product-title" style="left:30px;top:110px;font-size:46px;">PROTEINE<br><span class="accent">SHAKE</span></h1>
  <p class="product-flavour" style="left:32px;top:208px;font-size:23px;">CHOCOLATE</p>
  <div class="ring" role="img" aria-label="Soft golden line-pattern disc" style="left:32px;top:246px;width:38px;height:38px;"></div>
  <p class="benefit" style="top:294px;font-size:13px;">80% protein, with A, B1, B2, B3, B6, B12, and C. Protein promotes muscle gain and helps maintain muscle mass.*</p>
  <p class="category" style="top:358px;">DIETARY SUPPLEMENT</p>
  <p class="net-weight" style="top:380px;">Net Wt. 300 g (10.58oz)</p>
  <div class="wave-band" role="img" aria-label="Golden wavy-line pattern band"></div>
</section>

<section class="panel panel--back">
  <div class="ring" role="img" aria-label="Soft golden line-pattern disc" style="left:38px;top:18px;width:46px;height:46px;"></div>
  <div class="usage">
    <p class="usage__heading">SUGGESTED USE:</p>
    <p class="usage__text">As a dietary supplement take 1 (one) tablet 15-30 minutes before bed or as directed by your healthcare professional.</p>
    <p class="usage__heading">CAUTION:</p>
    <p class="usage__text">Do not exceed recommended dose. Pregnant or nursing mothers, children under the age of 18, and individuals with a known medical condition should consult a physician before using this or any dietary supplement.</p>
    <p class="usage__warning">Keep out of reach of children. Do not use if safety seal is damaged or missing. Store in a cool, dry place.</p>
    <p class="usage__note">* These statements have not been evaluated by the Food and Drug Administration. This product is not intended to diagnose, treat, cure or prevent any disease.</p>
  </div>
  <div class="wave-band" role="img" aria-label="Golden wavy-line pattern band"></div>
</section>

<section class="panel panel--wrap">
  <div class="wrap-col wrap-col--usage">
    <div class="ring" role="img" aria-label="Soft golden line-pattern disc" style="left:26px;top:-12px;width:46px;height:46px;"></div>
    <div class="usage">
      <p class="usage__heading">SUGGESTED USE:</p>
      <p class="usage__text">As a dietary supplement take 1 (one) tablet 15-30 minutes before bed or as directed by your healthcare professional.</p>
      <p class="usage__heading">CAUTION:</p>
      <p class="usage__text">Do not exceed recommended dose. Pregnant or nursing mothers, children under the age of 18, and individuals with a known medical condition should consult a physician before using this or any dietary supplement.</p>
      <p class="usage__warning">Keep out of reach of children. Do not use if safety seal is damaged or missing. Store in a cool, dry place.</p>
      <p class="usage__note">* These statements have not been evaluated by the Food and Drug Administration. This product is not intended to diagnose, treat, cure or prevent any disease.</p>
    </div>
  </div>

  <div class="wrap-col wrap-col--front">
    <div class="brand"><span class="brand__dot"></span>lanternfolk.life</div>
    <h2 class="product-title" style="left:30px;top:100px;font-size:38px;">PROTEINE<br><span class="accent">SHAKE</span></h2>
    <p class="product-flavour" style="left:32px;top:186px;font-size:20px;">CHOCOLATE</p>
    <div class="ring" role="img" aria-label="Soft golden line-pattern disc" style="left:32px;top:222px;width:34px;height:34px;"></div>
    <p class="benefit">80% protein, with A, B1, B2, B3, B6, B12, and C. Protein promotes muscle gain and helps maintain muscle mass.*</p>
    <p class="category">DIETARY SUPPLEMENT</p>
    <p class="net-weight">Net Wt. 300 g (10.58oz)</p>
  </div>

  <div class="wrap-col wrap-col--facts">
    <div class="facts">
      <p class="facts__title">Supplement Facts</p>
      <p class="facts__serving">Serving Size: 1 tablet<br>Servings per container: 60</p>
      <div class="facts__row facts__row--head">
        <span class="facts__name"></span>
        <span class="facts__amount">Amount per Serving</span>
        <span class="facts__dv">% Daily Value</span>
      </div>
      <div class="facts__row"><span class="facts__name">Calories</span><span class="facts__amount">0.076 Kcal</span><span class="facts__dv">*</span></div>
      <div class="facts__row facts__row--last"><span class="facts__name">Melatonin</span><span class="facts__amount">1000 µg</span><span class="facts__dv">*</span></div>
      <p class="facts__footnote">*Daily Value not established.</p>
    </div>
    <p class="ingredients">Other Ingredients: Microcrystalline cellulose, starch, magnesium salts of fatty acids and silica.</p>
    <div class="ring" role="img" aria-label="Soft golden line-pattern disc" style="left:28px;top:280px;width:50px;height:50px;"></div>
    <p class="maker">Manufactured for and distributed by:<br>[your LLC name here]<br>Address:<br>[your legal address and phone nr or email]</p>
  </div>

  <div class="wave-band" role="img" aria-label="Golden wavy-line pattern band"></div>
</section>

</body>
</html>
```